Cutting Costs Quickly - A Weekend Money Plan

Nonfiction book about how to save on insurance. Almost one hundred measures and examples to reduce ones insurance costs.

Target Market(s)

Men/Women between 18 and 50

Industry/Entity Type

Insurance

```html
<!DOCTYPE html>
<html lang="en">
<head>
<meta charset="utf-8">
<title>Cutting Costs Quickly - A Weekend Money Plan</title>
<link rel="stylesheet" href="https://fonts.googleapis.com/css2?family=Alfa+Slab+One&family=Open+Sans:wght@800&display=swap">
<style>
  :root {
    --paper: #ffffff;
    --ink: #111111;
    --red: #e3262c;
    --red-deep: #b8151b;
    --salmon: #f3a893;
    --art-light: #f3f3f3;
    --art-mid: #dedede;
    --art-dark: #c9c9c9;
  }
  html, body {
    margin: 0;
    padding: 0;
    width: 930px;
    height: 1200px;
    overflow: hidden;
    background: var(--paper);
  }
  .cover {
    position: relative;
    width: 930px;
    height: 1200px;
    background: var(--paper);
    font-family: "Alfa Slab One", Georgia, serif;
    color: var(--ink);
    text-align: center;
  }
  .title {
    margin: 0;
    padding-top: 105px;
    font-weight: 400;
    line-height: 1;
  }
  .title-line {
    display: block;
    letter-spacing: 1px;
  }
  .title-top {
    font-size: 130px;
  }
  .title-accent {
    font-size: 190px;
    line-height: 0.95;
    margin-top: 4px;
    background: linear-gradient(to bottom, var(--salmon) 0%, var(--salmon) 48%, var(--red) 48%, var(--red) 100%);
    -webkit-background-clip: text;
    background-clip: text;
    color: transparent;
  }
  .title-bottom {
    font-size: 116px;
    margin-top: 6px;
  }
  .subtitle-band {
    position: absolute;
    left: 0;
    top: 560px;
    width: 100%;
    height: 100px;
    background: linear-gradient(to right, var(--red-deep) 0%, var(--red) 40%, var(--red) 100%);
    display: flex;
    align-items: center;
    justify-content: center;
  }
  .subtitle {
    margin: 0;
    font-family: "Open Sans", Arial, sans-serif;
    font-weight: 800;
    font-size: 54px;
    letter-spacing: 1px;
    color: var(--paper);
  }
  .cover-art {
    position: absolute;
    left: 215px;
    top: 700px;
    width: 500px;
    height: 320px;
    border-radius: 16px;
    background: linear-gradient(to bottom, var(--art-light) 0%, var(--art-mid) 60%, var(--art-dark) 100%);
  }
  .author {
    position: absolute;
    left: 0;
    top: 1075px;
    width: 100%;
    margin: 0;
    font-size: 60px;
    font-weight: 400;
    line-height: 1;
    letter-spacing: 1px;
  }
</style>
</head>
<body>
  <main class="cover">
    <h1 class="title">
      <span class="title-line title-top">CUTTING</span>
      <span class="title-line title-accent">COSTS</span>
      <span class="title-line title-bottom">QUICKLY</span>
    </h1>
    <div class="subtitle-band">
      <p class="subtitle">A WEEKEND MONEY PLAN</p>
    </div>
    <div class="cover-art" role="img" aria-label="Photo area: silver stopwatch resting on a white and red life buoy"></div>
    <p class="author">AUTHOR NAME</p>
  </main>
</body>
</html>
```